Create Web Design Template with Source Files

I need a web design built with PSD/source files. See attached design I have made to guidance. Also I have attached an image I have used so you can use it.

I got my inspiration from this site if you would like to use it also:
http://zintaglo.com/home

PSD & html slicing and responsive designs also. So we can run across all devices.

1 page

• See attachments. Ask if you have any questions...

```html
<!DOCTYPE html>
<html lang="en">
<head>
<meta charset="utf-8">
<title>Vexlo — Home</title>
<link rel="stylesheet" href="https://fonts.googleapis.com/css2?family=Roboto:wght@300;400;500;700;900&family=Roboto+Slab:wght@300;400;700&display=swap">
<style>
:root{
  --purple:#8a0ab0;
  --green:#3f9e3a;
  --ink:#222222;
  --muted:#8a8a8a;
  --rule:#e6e6e6;
  --sidebar:#0d0d0d;
  --footer:#e4e4e4;
  --white:#ffffff;
}
*{box-sizing:border-box;margin:0;padding:0}
html,body{width:882px;height:1200px;overflow:hidden;background:var(--white)}
body{position:relative;font-family:"Roboto",sans-serif;color:var(--ink)}

.topbar{position:absolute;left:0;top:0;width:882px;height:61px;background:var(--white);z-index:2}
.back-btn{position:absolute;left:34px;top:22px;width:21px;height:21px;border-radius:50%;background:var(--purple);display:flex;align-items:center;justify-content:center}
.brand{position:absolute;left:66px;top:16px;display:flex;align-items:center;gap:7px}
.brand-dot{width:22px;height:22px;border-radius:50%;background:var(--purple)}
.brand-name{font-family:"Roboto",sans-serif;font-weight:900;font-size:25px;color:var(--ink);letter-spacing:.3px}
.search{position:absolute;left:501px;top:22px;width:215px;height:24px;border-bottom:1px solid #bdbdbd;font-size:10.5px;color:#777;padding-top:2px}
.search-btn{position:absolute;left:726px;top:20px;width:26px;height:26px;border-radius:50%;background:var(--purple);display:flex;align-items:center;justify-content:center}
.login{position:absolute;left:766px;top:16px;width:84px;height:30px;background:var(--purple);color:var(--white);font-size:11px;font-weight:500;display:flex;align-items:center;justify-content:center;gap:5px;border-radius:2px}

.sidebar{position:absolute;left:0;top:61px;width:201px;height:1139px;background:var(--sidebar)}
.sidebar-photo{position:absolute;left:0;top:0;width:201px;height:260px;background:linear-gradient(180deg,#3b3331 0%,#2a2422 40%,#151312 80%,#0d0d0d 100%)}
.nav{position:absolute;left:0;top:0;width:201px}
.nav-item{position:absolute;left:16px;width:169px;height:32px;display:flex;align-items:center;gap:5px;padding-left:21px;color:var(--white);font-size:10.5px}
.nav-item.is-active{background:var(--purple);border-radius:2px}

.hero{position:absolute;left:201px;top:61px;width:681px;height:257px;background:linear-gradient(180deg,#2f2628 0%,#3a2c2e 45%,#1f1a1b 100%)}

.section{position:absolute;left:226px;width:624px}
.section-title{font-family:"Roboto Slab",serif;font-weight:700;font-size:24px;color:var(--ink);line-height:1}
.subscribe{position:absolute;right:0;top:-9px;width:91px;height:25px;background:var(--green);color:var(--white);font-size:10.5px;display:flex;align-items:center;justify-content:center;gap:5px;border-radius:2px}
.section-lead{margin-top:12px;width:560px;font-size:10.5px;font-weight:300;color:var(--muted);line-height:19px}
.cards{position:absolute;left:0;top:80px;width:640px}
.card{position:absolute;top:0;width:148px}
.card-media{position:relative;width:148px;height:107px}
.duration{position:absolute;right:6px;bottom:6px;background:rgba(0,0,0,.8);color:var(--white);font-size:9.5px;padding:3px 6px}
.card-title{margin-top:11px;font-family:"Roboto Slab",serif;font-weight:300;font-size:11.5px;line-height:17px;color:var(--ink)}
.card-meta{margin-top:9px;display:flex;align-items:center;font-size:8px;color:var(--muted)}
.meta-mark{width:18px;height:12px;margin-right:5px;display:flex;align-items:center;justify-content:center}
.meta-date{margin-left:auto;margin-right:8px;font-style:italic;font-size:7.5px}
.load-more{position:absolute;left:260px;width:105px;height:30px;background:var(--purple);color:var(--white);font-size:10.5px;font-weight:700;display:flex;align-items:center;justify-content:center;gap:5px;border-radius:2px}
.divider{position:absolute;left:226px;top:708px;width:624px;height:1px;background:var(--rule)}

.footer{position:absolute;left:201px;top:1137px;width:681px;height:63px;background:var(--footer);font-size:9.5px;color:#444}
.footer-links{position:absolute;left:27px;top:25px;display:flex;gap:12px}
.footer-copy{position:absolute;right:32px;top:25px}
.footer-code{position:absolute;right:8px;top:25px}
</style>
</head>
<body>

<header class="topbar">
  <div class="back-btn"><svg width="8" height="8" viewBox="0 0 8 8"><path d="M5 1 2 4l3 3" fill="none" stroke="#fff" stroke-width="1.4"/></svg></div>
  <div class="brand"><span class="brand-dot"></span><span class="brand-name">Vexlo</span></div>
  <div class="search">Search</div>
  <div class="search-btn"><svg width="10" height="10" viewBox="0 0 10 10"><circle cx="4.2" cy="4.2" r="2.8" fill="none" stroke="#fff" stroke-width="1.4"/><path d="M6.3 6.3 8.6 8.6" stroke="#fff" stroke-width="1.6"/></svg></div>
  <div class="login"><svg width="9" height="9" viewBox="0 0 9 9"><circle cx="4.5" cy="2.5" r="2.2" fill="#fff"/><path d="M0.5 9a4 3.6 0 0 1 8 0z" fill="#fff"/></svg>LOG IN</div>
</header>

<aside class="sidebar">
  <div class="sidebar-photo" role="img" aria-label="Photo of a cheering crowd at a concert fading into the dark sidebar"></div>
  <nav class="nav">
    <div class="nav-item is-active" style="top:29px"><svg width="10" height="9" viewBox="0 0 10 9"><path d="M5 0 0 4.5h1.4V9h2.6V6h2v3h2.6V4.5H10z" fill="#fff"/></svg>Home</div>
    <div class="nav-item" style="top:77px"><svg width="7" height="9" viewBox="0 0 7 9"><path d="M1 2.8a2.5 2.3 0 1 1 3.6 2c-.8.4-1.1.8-1.1 1.6" fill="none" stroke="#fff" stroke-width="1.5"/><rect x="2.7" y="7.4" width="1.6" height="1.6" fill="#fff"/></svg>How it works</div>
    <div class="nav-item" style="top:124px"><svg width="9" height="9" viewBox="0 0 9 9"><circle cx="4.5" cy="2.5" r="2.2" fill="#fff"/><path d="M0.5 9a4 3.6 0 0 1 8 0z" fill="#fff"/></svg>About us</div>
    <div class="nav-item" style="top:170px"><svg width="10" height="9" viewBox="0 0 10 9"><path d="M2.5 0h5v3a2.5 2.5 0 0 1-5 0z M4.3 5.3h1.4v2h1.6V9H2.7V7.3h1.6z" fill="#fff"/><path d="M2.5 1H.6c0 1.8.9 2.6 2.2 2.8M7.5 1h1.9c0 1.8-.9 2.6-2.2 2.8" fill="none" stroke="#fff" stroke-width=".9"/></svg>Leaderboard</div>
    <div class="nav-item" style="top:219px"><svg width="11" height="9" viewBox="0 0 11 9"><ellipse cx="4.2" cy="3.2" rx="4.2" ry="3" fill="#fff"/><path d="M1.5 5.5 1 7.5l2.2-1.3z" fill="#fff"/><ellipse cx="7.4" cy="5.4" rx="3.4" ry="2.4" fill="#fff"/></svg>Weapons of comment</div>
  </nav>
</aside>

<div class="hero" role="img" aria-label="Photo of a crowd with raised hands at a live concert"></div>

<section class="section" style="top:352px">
  <h2 class="section-title">Foodies</h2>
  <div class="subscribe"><svg width="8" height="9" viewBox="0 0 8 9"><path d="M0 0h8v9L4 6.5 0 9z" fill="#fff"/></svg>SUBSCRIBE</div>
  <p class="section-lead">Nemo enim ipsam voluptatem qis autem vel eum iuro enim ipsam voluptatem qis autem vel eum iure repa oluptate velit esse quam nihil ia voluptiat quo voluptarehenderit qui in ea voluptate..</p>
  <div class="cards">
    <article class="card" style="left:0">
      <div class="card-media" role="img" aria-label="Photo of a pizza with olives and peppers" style="background:linear-gradient(135deg,#b5532a,#d9973f 55%,#7a3b1c)"><span class="duration">12 Sec</span></div>
      <h3 class="card-title">Nemo enim ipsam exea voluptatem</h3>
      <div class="card-meta"><span class="meta-mark"><svg width="14" height="10"><circle cx="7" cy="5" r="4.5" fill="none" stroke="#8a8a8a" stroke-width="1.2"/></svg></span>Foodies<span class="meta-date">2 days ago</span></div>
    </article>
    <article class="card" style="left:159px">
      <div class="card-media" role="img" aria-label="Photo of a plated fish cake topped with fresh greens" style="background:linear-gradient(135deg,#3a2a20,#7a5434 55%,#2c211b)"><span class="duration">1 min</span></div>
      <h3 class="card-title">Duis aute irure dolor inre prehenderit</h3>
      <div class="card-meta"><span class="meta-mark"><svg width="14" height="10"><circle cx="7" cy="5" r="4.5" fill="none" stroke="#8a8a8a" stroke-width="1.2"/></svg></span>Foodies<span class="meta-date">4 days ago</span></div>
    </article>
    <article class="card" style="left:318px">
      <div class="card-media" role="img" aria-label="Photo of sliced steak with herb sauce on a board" style="background:linear-gradient(135deg,#3b2a24,#7b5148 50%,#2f3a22)"><span class="duration">5 min</span></div>
      <h3 class="card-title">Ium dolore eu fugiat nulla pariatuillum</h3>
      <div class="card-meta"><span class="meta-mark"><svg width="14" height="10"><circle cx="7" cy="5" r="4.5" fill="none" stroke="#8a8a8a" stroke-width="1.2"/></svg></span>Foodies<span class="meta-date">3 days ago</span></div>
    </article>
    <article class="card" style="left:476px">
      <div class="card-media" role="img" aria-label="Photo of a restaurant table set with several dishes" style="background:linear-gradient(135deg,#4b4a4c,#c9a98a 50%,#d46a2c)"><span class="duration">23 Sec</span></div>
      <h3 class="card-title">Sunt in culpaqui officia ea commodo</h3>
      <div class="card-meta"><span class="meta-mark"><svg width="14" height="10"><circle cx="7" cy="5" r="4.5" fill="none" stroke="#8a8a8a" stroke-width="1.2"/></svg></span>Foodies<span class="meta-date">2 days ago</span></div>
    </article>
  </div>
  <div class="load-more" style="top:288px">LOAD MORE <svg width="10" height="10" viewBox="0 0 10 10"><circle cx="5" cy="5" r="5" fill="#fff"/><path d="M2.5 5h4M5 3l2 2-2 2" fill="none" stroke="#8a0ab0" stroke-width="1.3"/></svg></div>
</section>

<div class="divider"></div>

<section class="section" style="top:745px">
  <h2 class="section-title">Healthy Living</h2>
  <div class="subscribe"><svg width="8" height="9" viewBox="0 0 8 9"><path d="M0 0h8v9L4 6.5 0 9z" fill="#fff"/></svg>SUBSCRIBE</div>
  <p class="section-lead">Nemo enim ipsam voluptatem qis autem vel eum iuro enim ipsam voluptatem qis autem vel eum iure repa oluptate velit esse quam nihil ia voluptiat quo voluptarehenderit qui in ea voluptate..</p>
  <div class="cards" style="top:91px">
    <article class="card" style="left:0">
      <div class="card-media" role="img" aria-label="Photo of a person with raised arms facing a golden sunset" style="background:linear-gradient(180deg,#f2a43a,#f7c86a 45%,#c2491e)"><span class="duration">12 Sec</span></div>
      <h3 class="card-title">Illum dolore eu fugiat nulla pariatu</h3>
      <div class="card-meta"><span class="meta-mark"><svg width="12" height="10"><rect x="0" y="0" width="12" height="10" fill="#111"/></svg></span>AirPulse<span class="meta-date">2 days ago</span></div>
    </article>
    <article class="card" style="left:159px">
      <div class="card-media" role="img" aria-label="Photo of a mother and daughter eating green apples" style="background:linear-gradient(135deg,#ece7e2,#cfb39b 50%,#f4f1ec)"><span class="duration">1 min</span></div>
      <h3 class="card-title">Duis aute irure dolor inre prehenderit</h3>
      <div class="card-meta"><span class="meta-mark"><svg width="12" height="10"><rect x="0" y="0" width="12" height="10" fill="#111"/></svg></span>AirPulse<span class="meta-date">3 days ago</span></div>
    </article>
    <article class="card" style="left:318px">
      <div class="card-media" role="img" aria-label="Photo of an older couple riding bicycles in a park" style="background:linear-gradient(180deg,#7e9a3f,#3f6fb3 50%,#6b8a36)"><span class="duration">5 min</span></div>
      <h3 class="card-title">Aute irurepre hdetsmo eiusmod tempor</h3>
      <div class="card-meta"><span class="meta-mark"><svg width="12" height="10"><rect x="0" y="0" width="12" height="10" fill="#111"/></svg></span>AirPulse<span class="meta-date">2 days ago</span></div>
    </article>
    <article class="card" style="left:476px">
      <div class="card-media" role="img" aria-label="Photo of a smiling woman holding a glass of juice" style="background:linear-gradient(90deg,#f1f3f4,#c7b7a8 60%,#8a6a57)"><span class="duration">23 Sec</span></div>
      <h3 class="card-title">Sunt in culpaqui officia ea commodo</h3>
      <div class="card-meta"><span class="meta-mark"><svg width="12" height="10"><rect x="0" y="0" width="12" height="10" fill="#111"/></svg></span>AirPulse<span class="meta-date">4 days ago</span></div>
    </article>
  </div>
  <div class="load-more" style="top:288px">LOAD MORE <svg width="10" height="10" viewBox="0 0 10 10"><circle cx="5" cy="5" r="5" fill="#fff"/><path d="M2.5 5h4M5 3l2 2-2 2" fill="none" stroke="#8a0ab0" stroke-width="1.3"/></svg></div>
</section>

<footer class="footer">
  <div class="footer-links"><span>TERMS OF SERVICE</span><span>|</span><span>PRIVACY</span><span>|</span><span>COPYRIGHT</span></div>
  <div class="footer-copy">Copyright © 2018 Vexlo. All Rights Reserved.</div>
  <div class="footer-code">C9</div>
</footer>

</body>
</html>
```